Business Broker Website

This website will be for a business broker. The logo is attached and will need to be in the footer as it is but in the header please remove the word 'group' and replace with 'business sales' (so that it is marvello business sales).
It needs to be a modern high end corporate font for the logo and also for the rest of the site. Please only use fonts available on fonts.google.com
It needs to have 4 prominent boxes at the top of the page that say 'business listings', 'appraisal report', 'what we do' and 'who we are'
The 'what we do' section needs to have sub menu items for 'sectors' and 'services'. The who we are section needs to have sub menu items for 'about us' and 'team'
The top menu needs to have :
* Home
* Businesses for Sale
* Sell your Business
* What we do
* About Us
* Contact
This needs to be seen as the #1 business broker in Australia. It needs to attract serious high quality buyers and sellers and needs to be highly professional, premium and straight to the point and innovative.
It needs to show that Marvello Business Sales not only do SME sales but also do Corporate Mergers and Acquisitions.
They like the look of the site at https://brackwoodallies.example/en-us/
They also love the look of https://quorvenadvisers.example/ (they prefer this to the above site)
The website features a clean, minimalist layout with ample white space, making it easy to navigate and visually appealing. The typography is modern and legible, and the color palette is professional, enhancing the site's overall aesthetic. High-quality images and a responsive design contribute to its polished appearance.
Please note this is for an Australian based business.
Contact details to show in the footer:
Head Office
Suite 17, First Floor
48 Tamsin Street
Corrigan Flats
VIC 3412
1300 55 01 29
info@marvellogroup.example.au
If you need some wording for the site, look at https://www.marvellogroup.example.au/businesssales which is a page about their business division. Don't use all this content though as they want it straight to the point and not rambling on.

```html
<!DOCTYPE html>
<html lang="en">
<head>
<meta charset="utf-8">
<title>Marvello Business Sales</title>
<link rel="stylesheet" href="https://fonts.googleapis.com/css2?family=Lexend:wght@400;500;600&family=Roboto:wght@400;500;700&display=swap">
<style>
:root{
  --orange:#f04923;
  --navy:#1f3441;
  --navy-deep:#16232c;
  --bar:#0d1822;
  --ink:#2a3a45;
  --muted:#6b747a;
  --white:#ffffff;
  --line:#e4e7ea;
}
*{box-sizing:border-box;margin:0;padding:0}
html,body{width:1200px;height:3066px;overflow:hidden}
body{position:relative;background:var(--white);font-family:"Roboto",sans-serif;color:var(--ink)}
.abs{position:absolute}
.head{font-family:"Lexend",sans-serif}
svg.bg{position:absolute;left:0;top:0}

/* header */
.top-line{left:0;top:0;width:1200px;height:4px;background:var(--orange)}
.brand{left:111px;top:36px;display:flex;align-items:center;gap:14px}
.brand-dot{width:44px;height:44px;border-radius:50%;background:var(--orange)}
.brand-name{font-family:"Lexend",sans-serif;font-weight:600;color:var(--navy);font-size:26px;line-height:28px;text-transform:uppercase;letter-spacing:.5px}
.brand-name small{display:block;font-size:19px;line-height:24px}
.social-top{width:42px;height:42px;border-radius:50%;background:#fff;box-shadow:0 3px 10px rgba(0,0,0,.12)}
.phone-ico{left:693px;top:27px;width:43px;height:43px;border-radius:50%;background:var(--navy);display:flex;align-items:center;justify-content:center}
.call-label{left:759px;top:28px;font-size:10px;color:var(--muted)}
.call-num{left:759px;top:46px;font-size:19px;font-weight:500;color:var(--navy-deep)}
.btn-contact{left:951px;top:27px;width:136px;height:42px;border-radius:21px 0 21px 21px;background:var(--navy);color:#fff;font-size:15px;font-weight:500;display:flex;align-items:center;justify-content:center}
.nav-item{top:121px;font-size:15px;font-weight:700;color:#fff;text-transform:uppercase}
.nav-item.active{color:var(--navy)}

/* hero */
.hero-title{left:111px;top:236px;color:#fff;font-weight:500;text-transform:uppercase;letter-spacing:-.5px}
.hero-title .l1{display:block;font-size:52px;line-height:54px}
.hero-title .l2{display:block;font-size:40px;line-height:50px}
.hero-copy{left:111px;top:400px;width:460px;color:#fff;font-size:17.5px;line-height:29px}
.btn{display:flex;align-items:center;justify-content:center;border-radius:22px;font-size:17px;font-weight:500}
.btn-light{left:111px;top:483px;width:178px;height:41px;background:#fff;color:var(--orange)}
.btn-orange{left:307px;top:483px;width:216px;height:41px;background:var(--orange);color:#fff}
.support{left:1060px;top:514px;width:48px;height:48px;border-radius:50%;background:#fff;box-shadow:0 4px 12px rgba(0,0,0,.2);display:flex;align-items:center;justify-content:center}

/* edge */
.eyebrow{font-size:17px;font-weight:500;color:var(--orange);text-transform:uppercase}
.section-title{font-family:"Lexend",sans-serif;font-weight:600;font-size:40px;color:var(--navy);text-transform:uppercase;letter-spacing:-.5px}
.center{left:0;width:1200px;text-align:center}
.card{top:883px;width:234px;height:263px;background:#fff;border:1px solid var(--line);border-radius:42px;box-shadow:0 10px 30px rgba(0,0,0,.05)}
.card-icon{position:absolute;left:28px;top:34px;width:86px;height:86px;border-radius:50%;background:var(--navy);display:flex;align-items:center;justify-content:center}
.card h3{position:absolute;left:28px;top:141px;font-size:16px;font-weight:700;color:var(--navy);text-transform:uppercase}
.card p{position:absolute;left:28px;top:166px;width:186px;font-size:13.5px;line-height:23px;color:var(--muted)}

/* split */
.split-col{top:1323px;width:600px;text-align:center;color:#fff}
.split-col .kicker{font-size:17px;font-weight:700;text-transform:uppercase}
.split-col h2{font-family:"Lexend",sans-serif;font-weight:600;font-size:40px;line-height:48px;text-transform:uppercase}
.photo{border-radius:60px 60px 0 0}
.split-copy{top:1637px;width:420px;font-size:14.5px;line-height:26px;text-align:center;color:#fff}
.btn-sm{top:1734px;width:143px;height:41px;border-radius:21px;font-size:16px;font-weight:500;display:flex;align-items:center;justify-content:center;color:#fff}

/* about */
.about-photo{left:111px;top:1956px;width:488px;height:487px;border-radius:50% 50% 0 50%;background:linear-gradient(135deg,#e9ebec,#c9d0d6 55%,#9aa5b0)}
.about-text{left:677px;width:412px}
.about-body{font-size:14.5px;line-height:26.6px;color:var(--muted);text-align:justify}

/* footer */
.foot-brand{left:111px;top:2732px;width:240px;display:flex;align-items:center;gap:10px}
.foot-brand .dot{flex:none;width:36px;height:36px;border-radius:50%;background:var(--orange)}
.foot-brand span{font-family:"Lexend",sans-serif;font-weight:600;font-size:24px;line-height:30px;color:#fff;white-space:nowrap}
.social-foot{top:2804px;width:36px;height:36px;border-radius:50%;background:#fff}
.foot-h{top:2724px;font-family:"Lexend",sans-serif;font-weight:500;font-size:19px;color:#fff;text-transform:uppercase}
.foot-links{left:389px;top:2764px;list-style:none;font-size:15px;line-height:30px;color:#fff}
.foot-ico{left:586px;width:27px;height:27px;border-radius:50%;background:#fff;display:flex;align-items:center;justify-content:center}
.foot-txt{left:627px;font-size:15px;line-height:25.5px;color:#fff}
.sub-txt{left:864px;top:2762px;width:226px;font-size:14.5px;line-height:27px;color:#fff}
.sub-form{left:863px;top:2861px;width:227px;height:38px;border-radius:19px;background:#fff;overflow:hidden;display:flex;align-items:center}
.sub-form .ph{margin-left:50px;font-size:11.5px;color:var(--muted)}
.sub-form .go{position:absolute;right:0;top:0;width:48px;height:38px;background:var(--orange);display:flex;align-items:center;justify-content:center}
.bottom-bar{left:0;top:3009px;width:1200px;height:57px;background:var(--bar);color:#fff;font-size:13.5px}
</style>
</head>
<body>

<svg class="bg" width="1200" height="3066" viewBox="0 0 1200 3066" aria-hidden="true">
  <defs>
    <linearGradient id="heroTone" x1="0" y1="0" x2="1" y2="1">
      <stop offset="0" stop-color="#4a6a86"/>
      <stop offset=".5" stop-color="#2b4761"/>
      <stop offset="1" stop-color="#1b2f42"/>
    </linearGradient>
    <linearGradient id="sectorTone" x1="0" y1="0" x2="1" y2="1">
      <stop offset="0" stop-color="#2a3c48"/>
      <stop offset="1" stop-color="#1a2a34"/>
    </linearGradient>
    <linearGradient id="serviceTone" x1="0" y1="0" x2="1" y2="1">
      <stop offset="0" stop-color="#e8401c"/>
      <stop offset="1" stop-color="#f35a30"/>
    </linearGradient>
  </defs>
  <polygon points="0,127 1200,127 1200,520 333,652 0,562" fill="url(#heroTone)"/>
  <polygon points="0,562 333,652 1200,520 1200,534 333,693 0,572" fill="var(--orange)"/>
  <polygon points="0,1223 601,1295 601,1811 0,1880" fill="url(#sectorTone)"/>
  <polygon points="601,1295 1200,1223 1200,1880 601,1811" fill="url(#serviceTone)"/>
  <polygon points="0,2700 869,2535 1200,2645 1200,2664 869,2565 0,2706" fill="var(--orange)"/>
  <polygon points="0,2706 869,2565 1200,2664 1200,3009 0,3009" fill="var(--navy)"/>
  <polygon points="420,95 1200,95 1200,164 428,164 408,129" fill="var(--orange)"/>
</svg>

<div class="abs top-line"></div>
<div role="img" aria-label="City skyline at dusk with river bridge" class="abs" style="left:0;top:127px;width:1200px;height:1px"></div>

<div class="abs brand">
  <div class="brand-dot"></div>
  <div class="brand-name">Marvello<small>Business Sales</small></div>
</div>
<a class="abs social-top" style="left:509px;top:28px" aria-label="Facebook"></a>
<a class="abs social-top" style="left:563px;top:28px" aria-label="Instagram"></a>
<a class="abs social-top" style="left:616px;top:28px" aria-label="YouTube"></a>
<div class="abs phone-ico">
  <svg width="16" height="16" viewBox="0 0 24 24"><path fill="#fff" d="M6.6 10.8a15.1 15.1 0 0 0 6.6 6.6l2.2-2.2a1 1 0 0 1 1-.25 11.4 11.4 0 0 0 3.6.57 1 1 0 0 1 1 1V20a1 1 0 0 1-1 1A17 17 0 0 1 3 4a1 1 0 0 1 1-1h3.5a1 1 0 0 1 1 1c0 1.25.2 2.45.57 3.57a1 1 0 0 1-.25 1z"/></svg>
</div>
<div class="abs call-label">CALL US:</div>
<div class="abs call-num">+61 1300 550 129</div>
<div class="abs btn-contact">Contact Us</div>

<nav>
  <span class="abs nav-item active" style="left:458px">Home</span>
  <span class="abs nav-item" style="left:531px">About Us</span>
  <span class="abs nav-item" style="left:631px">Businesses for Sale</span>
  <span class="abs nav-item" style="left:819px">Sell Your Business</span>
  <span class="abs nav-item" style="left:996px">What We Do</span>
</nav>

<h1 class="abs hero-title head">
  <span class="l1">Buy or Sell</span>
  <span class="l2">A Business Confidently</span>
  <span class="l2">At the Right Price.</span>
</h1>
<p class="abs hero-copy">We help owners exit and buyers invest — with expert guidance, clear valuations, &amp; successful outcomes.</p>
<div class="abs btn btn-light">See What's New</div>
<div class="abs btn btn-orange">Explore Our Services</div>
<div class="abs support">
  <svg width="20" height="20" viewBox="0 0 24 24" fill="none" stroke="var(--navy)" stroke-width="2.4"><path d="M4 15v-3a8 8 0 0 1 16 0v3"/><rect x="3" y="14" width="4" height="6" rx="1" fill="var(--navy)"/><rect x="17" y="14" width="4" height="6" rx="1" fill="var(--navy)"/></svg>
</div>

<div class="abs center eyebrow" style="top:781px">Excellence in Every Transaction</div>
<h2 class="abs center section-title" style="top:806px">Our Competitive Edge</h2>

<div class="abs card" style="left:111px">
  <div class="card-icon"><svg width="38" height="40" viewBox="0 0 24 26" fill="none" stroke="#fff" stroke-width="2"><rect x="4" y="3" width="16" height="21" rx="2"/><path d="M8 9l1.5 1.5L12 8M8 14l1.5 1.5L12 13M8 19l1.5 1.5L12 18M14 9h3M14 14h3M14 19h3"/></svg></div>
  <h3>Business Listings</h3>
  <p>Browse curated businesses for sale — from SMEs to corporate deals.</p>
</div>
<div class="abs card" style="left:358px">
  <div class="card-icon"><svg width="40" height="40" viewBox="0 0 24 24" fill="none" stroke="#fff" stroke-width="2"><circle cx="8" cy="8" r="5"/><path d="M8 3v5h5"/><rect x="11" y="11" width="10" height="11" rx="1"/><path d="M14 19v-2M16 19v-4M18 19v-3"/></svg></div>
  <h3>Appraisal Report</h3>
  <p>Accurate, confidential appraisal reports for informed decisions.</p>
</div>
<div class="abs card" style="left:607px">
  <div class="card-icon"><svg width="40" height="40" viewBox="0 0 24 24" fill="none" stroke="#fff" stroke-width="2"><circle cx="6" cy="6" r="2.5"/><path d="M10 13l3-3 2 2 5-5M17 7h3v3M3 18l4-2h5a2 2 0 0 1 0 4H8M12 18l6-3a1.5 1.5 0 0 1 2 2l-6 5H6"/></svg></div>
  <h3>What We Do</h3>
  <p>We provide end-to-end advisory for business sales, mergers, &amp; acquisitions.</p>
</div>
<div class="abs card" style="left:855px">
  <div class="card-icon"><svg width="42" height="40" viewBox="0 0 26 24" fill="#fff"><path d="M13 2l5 2v4c0 3-2 5-5 6-3-1-5-3-5-6V4z"/><path d="M11 7.5l1.5 1.5 3-3" stroke="var(--navy)" stroke-width="1.6" fill="none"/><circle cx="5" cy="15" r="2.5"/><circle cx="13" cy="17" r="2.5"/><circle cx="21" cy="15" r="2.5"/><path d="M1 22c0-2 2-3.5 4-3.5s4 1.5 4 3.5zM9 24c0-2 2-3.5 4-3.5s4 1.5 4 3.5zM17 22c0-2 2-3.5 4-3.5s4 1.5 4 3.5z"/></svg></div>
  <h3>Who We Are</h3>
  <p>We're trusted advisors with decades of experience guiding business owners.</p>
</div>

<div class="abs split-col" style="left:0">
  <div class="kicker">What We Do</div>
  <h2>Sectors</h2>
</div>
<div class="abs photo" role="img" aria-label="Diners seated around tables in a busy restaurant" style="left:94px;top:1411px;width:405px;height:203px;background:linear-gradient(135deg,#8a5a3a,#c49a6c 50%,#5b6a4a)"></div>
<p class="abs split-copy" style="left:86px">Except to obtain some advantage from it? But who has any right to find fault with a man who chooses to enjoy a pleasure that has no annoying consequences</p>
<div class="abs btn-sm" style="left:225px;background:var(--orange)">Learn More</div>

<div class="abs split-col" style="left:607px">
  <div class="kicker">What We Do</div>
  <h2>Services</h2>
</div>
<div class="abs photo" role="img" aria-label="Modern school building facade with a pink glass entrance" style="left:702px;top:1411px;width:405px;height:203px;background:linear-gradient(90deg,#5f7f99,#d8336e 45%,#c2345f 60%,#6f8aa0)"></div>
<p class="abs split-copy" style="left:694px">Except to obtain some advantage from it? But who has any right to find fault with a man who chooses to enjoy a pleasure that has no annoying consequences</p>
<div class="abs btn-sm" style="left:833px;background:var(--navy)">Learn More</div>

<div class="abs about-photo" role="img" aria-label="Three business professionals reviewing a document together in a bright office"></div>
<div class="abs about-text eyebrow" style="top:1990px">Who We Are</div>
<h2 class="abs about-text section-title" style="top:2012px">About Us</h2>
<div class="abs about-text" style="top:2072px;font-size:16.5px;font-weight:700;color:var(--navy)">The Right Expertise for the Job</div>
<p class="abs about-text about-body" style="top:2102px">When you're looking to sell or lease your property, whether commercial, industrial or residential, we know that it has to be presented in a way so as to make it as attractive as possible to potential buyers or lessees.</p>
<p class="abs about-text about-body" style="top:2226px">Our carefully selected team of salespeople, photographers, designers and marketing specialists are highly-regarded professionals in their fields, ensuring our ability to offer you the best quality representation.</p>
<div class="abs btn" style="left:677px;top:2365px;width:144px;height:42px;background:var(--orange);color:#fff">Learn More</div>

<div class="abs foot-brand"><div class="dot"></div><span>Marvello Group</span></div>
<a class="abs social-foot" style="left:108px" aria-label="Facebook"></a>
<a class="abs social-foot" style="left:150px" aria-label="Instagram"></a>
<a class="abs social-foot" style="left:190px" aria-label="LinkedIn"></a>
<a class="abs social-foot" style="left:231px" aria-label="YouTube"></a>

<div class="abs foot-h" style="left:389px">Quick Links</div>
<ul class="abs foot-links">
  <li>Home</li><li>Businesses for Sale</li><li>Sell Your Business</li><li>What We Do</li><li>About Us</li><li>Contact</li>
</ul>

<div class="abs foot-h" style="left:589px">Contact Us</div>
<div class="abs foot-ico" style="top:2769px"><svg width="12" height="12" viewBox="0 0 24 24"><path fill="var(--navy)" d="M6.6 10.8a15.1 15.1 0 0 0 6.6 6.6l2.2-2.2a1 1 0 0 1 1-.25 11.4 11.4 0 0 0 3.6.57 1 1 0 0 1 1 1V20a1 1 0 0 1-1 1A17 17 0 0 1 3 4a1 1 0 0 1 1-1h3.5a1 1 0 0 1 1 1c0 1.25.2 2.45.57 3.57a1 1 0 0 1-.25 1z"/></svg></div>
<div class="abs foot-txt" style="top:2770px">+61 1300 550 129</div>
<div class="abs foot-ico" style="top:2810px"><svg width="12" height="12" viewBox="0 0 24 24"><path fill="var(--navy)" d="M2 5h20v14H2z"/><path d="M2 5l10 8 10-8" stroke="#fff" stroke-width="2" fill="none"/></svg></div>
<div class="abs foot-txt" style="top:2810px">info@marvellogroup.example.au</div>
<div class="abs foot-ico" style="top:2850px"><svg width="12" height="12" viewBox="0 0 24 24"><path fill="var(--navy)" d="M12 2a7 7 0 0 0-7 7c0 5 7 13 7 13s7-8 7-13a7 7 0 0 0-7-7zm0 9.5a2.5 2.5 0 1 1 0-5 2.5 2.5 0 0 1 0 5z"/></svg></div>
<div class="abs foot-txt" style="top:2850px">Suite 17, First Floor,<br>48 Tamsin Street, Corrigan<br>Flats, VIC, Australia,<br>Victoria</div>

<div class="abs foot-h" style="left:857px">Subscribe to our Blog</div>
<p class="abs sub-txt">Sign up today to get resources on how to attract and retain more customers!</p>
<div class="abs sub-form">
  <svg class="abs" style="left:22px;top:13px" width="14" height="12" viewBox="0 0 24 20" fill="none" stroke="var(--muted)" stroke-width="2"><rect x="2" y="2" width="20" height="16"/><path d="M2 2l10 8 10-8"/></svg>
  <span class="ph">Email Address</span>
  <div class="go"><svg width="18" height="18" viewBox="0 0 24 24"><path fill="#fff" d="M22 2L2 10l7 3 3 7z"/></svg></div>
</div>

<div class="abs bottom-bar">
  <span class="abs" style="left:111px;top:20px">Copyright© 2025 &nbsp;|&nbsp; All Rights Reserved</span>
  <span class="abs" style="left:844px;top:20px">Terms and Conditions &nbsp;&nbsp;|&nbsp;&nbsp; Privacy Policy</span>
</div>

</body>
</html>
```